Business Card Design

Provide project management services to the construction and other industries
Construction services - Civil and Concrete works
Shop Detailing
Structural Modelling
Client side coordination of project teams and consultants
Feasibility Studies for construction projects

Industry/Entity Type

Business

Contact Information for Business Card

Plan Sure
Derek Calloway B.Sc (Eng), M.Proj.Mgt.
Director

m: 0412 738 564
e: dcalloway@plansure.com.au

p: 08 6358 2714
a: 17 Banksia Court, Hillcrest, WA 6107

```html
<!DOCTYPE html>
<html lang="en">
<head>
<meta charset="utf-8">
<title>Plan Sure – Business Card</title>
<link rel="stylesheet" href="https://fonts.googleapis.com/css2?family=Open+Sans:wght@400;600;700;800&display=swap">
<style>
  :root {
    --green: #2fa36b;
    --green-deep: #127a3f;
    --green-dark: #0b5e30;
    --charcoal: #3f4144;
    --ink: #4a4c4f;
    --paper: #ffffff;
    --backdrop: #e9eae8;
  }
  * { box-sizing: border-box; margin: 0; padding: 0; }
  html, body { width: 1200px; height: 1023px; overflow: hidden; }
  body {
    background: var(--backdrop);
    font-family: "Open Sans", Arial, sans-serif;
    position: relative;
  }
  .card {
    position: absolute;
    width: 560px;
    height: 340px;
    border-radius: 4px;
    box-shadow: 0 10px 30px rgba(0,0,0,.18);
    overflow: hidden;
  }
  /* Front */
  .card-front {
    left: 60px; top: 120px;
    background: var(--paper);
    border-bottom: 8px solid var(--green);
  }
  .brand {
    position: absolute;
    left: 36px; top: 154px;
    display: flex; align-items: center; gap: 10px;
  }
  .brand-mark {
    width: 28px; height: 28px;
    background: var(--green);
  }
  .brand-name {
    font-weight: 800;
    font-size: 24px;
    color: var(--charcoal);
    letter-spacing: 1px;
    text-transform: uppercase;
    white-space: nowrap;
  }
  .details {
    position: absolute;
    left: 290px; top: 70px;
  }
  .person-name {
    font-size: 22px; font-weight: 600;
    color: var(--green);
    letter-spacing: .5px;
    text-transform: uppercase;
    white-space: nowrap;
  }
  .credentials { font-size: 12.5px; color: var(--green); margin-top: 2px; }
  .role { font-size: 12.5px; color: var(--ink); margin-top: 6px; letter-spacing: .5px; }
  .contact-list { list-style: none; margin-top: 14px; }
  .contact-list li {
    display: flex; align-items: center; gap: 8px;
    font-size: 12.5px; color: var(--ink);
    margin-bottom: 7px;
    white-space: nowrap;
  }
  .contact-icon {
    width: 14px; height: 14px; flex: none;
    display: block;
  }
  /* Back */
  .card-back {
    left: 600px; top: 560px;
    background: linear-gradient(135deg, var(--green-deep) 0%, var(--green) 55%, var(--green-dark) 100%);
    color: var(--paper);
  }
  .back-brand {
    position: absolute; left: 40px; top: 60px;
  }
  .back-rule {
    width: 230px; height: 5px; background: var(--paper);
    margin-bottom: 10px;
  }
  .back-name {
    font-weight: 800; font-size: 38px;
    letter-spacing: 2px; text-transform: uppercase;
  }
  .services {
    position: absolute; left: 40px; top: 170px;
    list-style: none;
  }
  .services li {
    font-size: 14px; line-height: 1.55;
    padding-left: 14px; position: relative;
  }
  .services li::before {
    content: ""; position: absolute; left: 0; top: 8px;
    width: 6px; height: 6px; border-radius: 50%;
    background: var(--paper);
  }
</style>
</head>
<body>
  <section class="card card-front" aria-label="Business card front">
    <div class="brand">
      <span class="brand-mark"></span>
      <span class="brand-name">Plan Sure</span>
    </div>
    <div class="details">
      <h1 class="person-name">Derek Calloway</h1>
      <p class="credentials">B.Sc (Eng), M.Proj.Mgt.</p>
      <p class="role">DIRECTOR</p>
      <ul class="contact-list">
        <li>
          <svg class="contact-icon" viewBox="0 0 14 14" aria-hidden="true"><rect width="14" height="14" rx="2" fill="#2fa36b"/><path d="M4 3.5l1.6 0 .7 2-1 .8a5 5 0 0 0 2.4 2.4l.8-1 2 .7v1.6c-3.5.4-7-3-6.5-6.5z" fill="#fff"/></svg>
          08 6358 2714
        </li>
        <li>
          <svg class="contact-icon" viewBox="0 0 14 14" aria-hidden="true"><rect width="14" height="14" rx="2" fill="#2fa36b"/><rect x="4.5" y="2.5" width="5" height="9" rx="1" fill="#fff"/><rect x="5.5" y="3.8" width="3" height="5.5" fill="#2fa36b"/></svg>
          0412 738 564
        </li>
        <li>
          <svg class="contact-icon" viewBox="0 0 14 14" aria-hidden="true"><rect width="14" height="14" rx="2" fill="#2fa36b"/><rect x="3" y="4" width="8" height="6" fill="#fff"/><path d="M3 4l4 3.2L11 4" stroke="#2fa36b" stroke-width="1" fill="none"/></svg>
          dcalloway@plansure.com.au
        </li>
        <li>
          <svg class="contact-icon" viewBox="0 0 14 14" aria-hidden="true"><rect width="14" height="14" rx="2" fill="#2fa36b"/><path d="M7 2.5a3 3 0 0 1 3 3c0 2.2-3 5.8-3 5.8S4 7.7 4 5.5a3 3 0 0 1 3-3z" fill="#fff"/><circle cx="7" cy="5.5" r="1" fill="#2fa36b"/></svg>
          17 Banksia Court, Hillcrest, WA 6107
        </li>
      </ul>
    </div>
  </section>

  <section class="card card-back" aria-label="Business card back">
    <div class="back-brand">
      <div class="back-rule"></div>
      <div class="back-name">Plan Sure</div>
    </div>
    <ul class="services">
      <li>Client side coordination of project teams and consultants</li>
      <li>Feasibility Studies for construction projects</li>
      <li>Civil and Concrete works</li>
      <li>Structural Modelling</li>
      <li>Shop Detailing</li>
    </ul>
  </section>
</body>
</html>
```